Creative Brief
Buisness Card Larkfield Homes
Card for Larkfield
Professional
Cal Dorsey
Constrution Supervisor
Larkfield Homes
PO Box 530618
Houston, Texas 77064
cdorsey@larkfield-homes.example
www.larkfield-homes.example
Logo file

```html
<!DOCTYPE html>
<html lang="en">
<head>
<meta charset="utf-8">
<title>Larkfield Homes — Business Card</title>
<link rel="stylesheet" href="https://fonts.googleapis.com/css2?family=Arimo:wght@400;700&display=swap">
<style>
  :root {
    --page-bg: #d9d9d6;
    --card-black: #050505;
    --card-sheen: #1c1c1c;
    --gold: #e6a317;
    --gold-light: #f5c451;
    --text-light: #e8e8e8;
    --text-muted: #bdbdbd;
  }
  html, body {
    margin: 0;
    padding: 0;
    width: 1200px;
    height: 901px;
    overflow: hidden;
    background: var(--page-bg);
    font-family: "Arimo", Arial, sans-serif;
  }
  .canvas {
    position: relative;
    width: 1200px;
    height: 901px;
  }
  .card {
    position: absolute;
    left: 250px;
    width: 700px;
    height: 400px;
    background: linear-gradient(125deg, var(--card-black) 0%, var(--card-black) 52%, var(--card-sheen) 53%, #0c0c0c 100%);
    box-shadow: 0 6px 18px rgba(0,0,0,0.35);
    overflow: hidden;
  }
  .card-front { top: 40px; }
  .card-back  { top: 461px; }

  .brand {
    display: flex;
    align-items: center;
    gap: 14px;
  }
  .brand-square {
    width: 26px;
    height: 26px;
    background: var(--gold);
    flex: none;
  }
  .brand-name {
    color: var(--gold);
    font-weight: 700;
    font-size: 30px;
    letter-spacing: 1px;
    white-space: nowrap;
  }
  .card-front .brand {
    position: absolute;
    left: 44px;
    top: 110px;
  }
  .card-front .brand-name { font-size: 26px; }

  .divider {
    position: absolute;
    left: 300px;
    top: 60px;
    width: 1px;
    height: 280px;
    background: linear-gradient(to bottom, transparent, #555 20%, #555 80%, transparent);
  }

  .contact {
    position: absolute;
    left: 340px;
    top: 64px;
    color: var(--text-light);
  }
  .person-name {
    margin: 0;
    color: var(--gold-light);
    font-weight: 700;
    font-size: 30px;
  }
  .person-title {
    margin: 4px 0 18px;
    font-size: 16px;
    color: var(--text-light);
  }
  .address {
    margin: 0 0 24px;
    font-size: 15px;
    line-height: 1.45;
    color: var(--text-muted);
  }
  .contact-list {
    list-style: none;
    margin: 0;
    padding: 0;
    font-size: 15px;
    line-height: 1;
  }
  .contact-list li {
    display: flex;
    align-items: center;
    gap: 10px;
    margin-bottom: 9px;
  }
  .contact-icon {
    width: 16px;
    height: 16px;
    flex: none;
  }
  .website { font-size: 17px; margin-top: 6px; }

  .card-back .brand {
    position: absolute;
    left: 50%;
    top: 50%;
    transform: translate(-50%, -50%);
  }
</style>
</head>
<body>
<main class="canvas">
  <section class="card card-front" aria-label="Business card front">
    <div class="brand">
      <span class="brand-square"></span>
      <span class="brand-name">Larkfield Homes</span>
    </div>
    <div class="divider"></div>
    <div class="contact">
      <h1 class="person-name">Cal Dorsey</h1>
      <p class="person-title">Construction Supervisor</p>
      <p class="address">Larkfield Homes<br>PO Box 530618<br>Houston, Texas 77064</p>
      <ul class="contact-list">
        <li>
          <svg class="contact-icon" viewBox="0 0 16 16"><circle cx="8" cy="8" r="8" fill="var(--gold)"/><path d="M5 4.5l1.6-.6 1 2-1 .8c.4 1 1.2 1.8 2.2 2.2l.8-1 2 1-.6 1.6c-3 .2-6.2-3-6-6z" fill="#000"/></svg>
          <span>281-555-0148</span>
        </li>
        <li>
          <svg class="contact-icon" viewBox="0 0 16 16"><circle cx="8" cy="8" r="8" fill="var(--gold)"/><path d="M5 4.5l1.6-.6 1 2-1 .8c.4 1 1.2 1.8 2.2 2.2l.8-1 2 1-.6 1.6c-3 .2-6.2-3-6-6z" fill="#000"/></svg>
          <span>832-555-0192</span>
        </li>
        <li>
          <svg class="contact-icon" viewBox="0 0 16 16"><circle cx="8" cy="8" r="8" fill="var(--gold)"/><rect x="4" y="5.5" width="8" height="5.5" fill="none" stroke="#000" stroke-width="1.1"/><path d="M4 5.5l4 3 4-3" fill="none" stroke="#000" stroke-width="1.1"/></svg>
          <span>cdorsey@larkfield-homes.example</span>
        </li>
        <li class="website">
          <svg class="contact-icon" viewBox="0 0 16 16"><circle cx="8" cy="8" r="8" fill="var(--gold)"/><circle cx="8" cy="8" r="4" fill="none" stroke="#000" stroke-width="1.1"/><path d="M4 8h8M8 4c-1.6 2.2-1.6 5.8 0 8M8 4c1.6 2.2 1.6 5.8 0 8" fill="none" stroke="#000" stroke-width="0.9"/></svg>
          <span>www.larkfield-homes.example</span>
        </li>
      </ul>
    </div>
  </section>

  <section class="card card-back" aria-label="Business card back">
    <div class="brand">
      <span class="brand-square"></span>
      <span class="brand-name">Larkfield Homes</span>
    </div>
  </section>
</main>
</body>
</html>
```